Dune Air & Plus business card

I need an awesome, double-sided business card designed with our new logo. I would like the one side black with the colored logo, and the back side is all yours. I'd like to see horizontal and vertical layouts. Get creative! Thank you.

Target Market(s)

HVAC, Heating and Cooling in Phoenix, AZ

Industry/Entity Type

HVAC

Contact Information for Business Card

We need our new logo on the card. Tom Harker, (623) 555-0142, tom@trydunesair.com, www.trydunesair.com, ROC 514273

```html
<!DOCTYPE html>
<html lang="en">
<head>
<meta charset="utf-8">
<title>Dune Air &amp; Plus — Business Card</title>
<link rel="stylesheet" href="https://fonts.googleapis.com/css2?family=Saira:wght@400;500;600&display=swap">
<style>
  :root {
    --bg: #e6e6e6;
    --card-white: #fbfbfb;
    --card-black: #0a0a0a;
    --panel-dark: #141414;
    --panel-mid: #262626;
    --text-light: #ffffff;
    --text-dark: #1a1a1a;
    --accent-red: #e8401c;
    --accent-blue: #1f5fbf;
  }
  * { margin: 0; padding: 0; box-sizing: border-box; }
  html, body {
    width: 800px; height: 1200px; overflow: hidden;
    background: var(--bg);
    font-family: "Saira", sans-serif;
  }
  .stage { position: relative; width: 800px; height: 1200px; }
  .card {
    position: absolute; top: 311px;
    width: 330px; height: 578px;
    box-shadow: 0 8px 24px rgba(0,0,0,0.18);
    overflow: hidden;
  }
  .card--front { left: 55px; background: var(--card-white); }
  .card--back  { left: 415px; background: var(--card-black); }

  .front-panel { position: absolute; inset: 0; }
  .name-block {
    position: absolute; top: 78px; left: 0; right: 0;
    text-align: center; color: var(--text-light);
  }
  .name { font-size: 42px; font-weight: 600; line-height: 1; letter-spacing: -0.5px; }
  .role { margin-top: 8px; font-size: 11px; font-weight: 500; letter-spacing: 2.5px; }
  .license {
    position: absolute; top: 355px; left: 70px;
    color: var(--accent-red); font-size: 17px; font-weight: 500;
  }
  .contact {
    position: absolute; top: 468px; left: 0; right: 0;
    text-align: center; color: var(--text-dark);
  }
  .contact-icons { display: flex; justify-content: center; gap: 28px; margin-bottom: 6px; }
  .contact-line { font-size: 15px; font-weight: 500; line-height: 1.35; }

  .back-texture { position: absolute; inset: 0; }
  .brand {
    position: absolute; top: 260px; left: 0; right: 0;
    display: flex; align-items: center; justify-content: center; gap: 10px;
    color: var(--text-light);
  }
  .brand-dot { width: 14px; height: 14px; border-radius: 50%; background: var(--text-light); }
  .brand-name { font-size: 28px; font-weight: 600; letter-spacing: 0.5px; }
  .website {
    position: absolute; bottom: 28px; left: 0; right: 0;
    text-align: center; color: var(--text-light);
    font-size: 16px; font-weight: 600;
  }
</style>
</head>
<body>
<main class="stage">

  <section class="card card--front" aria-label="Card front">
    <svg class="front-panel" width="330" height="578" viewBox="0 0 330 578" role="img" aria-label="Dark panel with diagonal carbon stripe texture">
      <defs>
        <linearGradient id="panelShade" x1="0" y1="0" x2="1" y2="1">
          <stop offset="0" stop-color="var(--panel-mid)"/>
          <stop offset="0.5" stop-color="var(--panel-dark)"/>
          <stop offset="1" stop-color="var(--panel-mid)"/>
        </linearGradient>
      </defs>
      <path d="M40 18 H290 Q312 18 312 40 V420 Q312 442 290 442 H120 L18 370 V40 Q18 18 40 18 Z" fill="url(#panelShade)"/>
    </svg>

    <div class="name-block">
      <h1 class="name">Tom Harker</h1>
      <p class="role">OWNER | MANAGER</p>
    </div>
    <p class="license">ROC 514273</p>

    <div class="contact">
      <div class="contact-icons">
        <svg width="16" height="18" viewBox="0 0 24 24" aria-hidden="true">
          <path fill="var(--accent-blue)" d="M6.6 10.8c1.4 2.8 3.8 5.1 6.6 6.6l2.2-2.2c.3-.3.7-.4 1-.2 1.1.4 2.3.6 3.6.6.6 0 1 .4 1 1V20c0 .6-.4 1-1 1C10.6 21 3 13.4 3 4c0-.6.4-1 1-1h3.5c.6 0 1 .4 1 1 0 1.3.2 2.5.6 3.6.1.3 0 .7-.2 1l-2.3 2.2z"/>
        </svg>
        <svg width="20" height="16" viewBox="0 0 24 18" aria-hidden="true">
          <rect x="1" y="1" width="22" height="16" rx="1.5" fill="var(--accent-blue)"/>
          <path d="M1.5 2 L12 10 L22.5 2" stroke="var(--card-white)" stroke-width="1.6" fill="none"/>
        </svg>
      </div>
      <p class="contact-line">(623) 555-0142</p>
      <p class="contact-line">tom@trydunesair.com</p>
    </div>
  </section>

  <section class="card card--back" aria-label="Card back">
    <svg class="back-texture" width="330" height="578" viewBox="0 0 330 578" role="img" aria-label="Black background with diagonal carbon stripe texture">
      <defs>
        <radialGradient id="backGlow" cx="0.5" cy="0.4" r="0.7">
          <stop offset="0" stop-color="#2a2a2a"/>
          <stop offset="1" stop-color="var(--card-black)"/>
        </radialGradient>
      </defs>
      <rect width="330" height="578" fill="url(#backGlow)"/>
    </svg>

    <div class="brand">
      <span class="brand-dot"></span>
      <span class="brand-name">Dune Air &amp; Plus</span>
    </div>
    <p class="website">www.trydunesair.com</p>
  </section>

</main>
</body>
</html>
```